3 Beispiel-Abbildungen für shop Kategorien
Zielgruppe
Entscheider und Ihre AssistentInnen im Marketing / Vertrieb von Firmen aller Branchen und Größen
Aufgabenstellung
Für einen B2B shop benötigen wir Piktogramme / Abbildungen / Grafiken für Kategorien (Produktlinien, Produktgruppen, Dienstleistungen...)
Mit einer eigenständig entwickelten Navi führen wir den Kunden direkt zu den Produkten und zeigen dabei immer die Alternativen. Viel Wert haben wir auf die Aktikelbeschreibungen und Abbildungen gelegt. Fuchsgrund.de will ein Fachgeschäft im Internet sein.
Die Abbildungen sollen aus einem Guß sein und zum CI der Seite passen. Da es am Ende ca. 300 Abbildungen sein werden, (mache sind doppelt, viele unterscheiden sich nur wenig) muss das Konzept einfach sein. Die Gesamt-Kosten sollten sich taxieren lassen und die Realisiierung sollte in insgesamt 8-12 Wochen hochgeladen sein.
Der Designer / die Desingerin sollte davon ausgehen, dass auch die Folgeaufträge zu machen (oder zu vergeben) sind.

```html
<!DOCTYPE html>
<html lang="de">
<head>
<meta charset="utf-8">
<title>Landkarten – Kategorien</title>
<link rel="stylesheet" href="https://fonts.googleapis.com/css2?family=Arimo:wght@400;700&family=Open+Sans:wght@400&display=swap">
<style>
  :root{
    --page-blue:#0b80b6;
    --head-dark:#0d2c4f;
    --head-mid:#1d4f7c;
    --green:#8cc34a;
    --green-dark:#6fa832;
    --green-pale:#e6f2d8;
    --icon-green:#74ae3b;
    --line:#d9d9d9;
    --text:#333333;
    --white:#ffffff;
    --map-orange:#f7a21c;
    --map-light:#ffc452;
    --map-deep:#e0861a;
  }
  *{box-sizing:border-box;margin:0;padding:0}
  html,body{width:1200px;height:481px;overflow:hidden}
  body{background:var(--page-blue);font-family:"Arimo",Arial,sans-serif;color:var(--text);position:relative}
  .column{position:absolute;top:16px;background:var(--white);height:465px;overflow:hidden}
  .col-shop{left:19px;width:299px}
  .col-market{left:323px;width:299px}
  .col-world{left:628px;width:561px;height:441px}
  .banner{height:181px;position:relative;background:radial-gradient(ellipse at 45% 30%,var(--head-mid),var(--head-dark) 75%);overflow:hidden}
  .cat-icon{position:absolute;width:86px;height:86px;border-radius:8px;border:2px solid #4b7a23;
    background:radial-gradient(circle at 50% 50%,#a9d86a,var(--icon-green) 70%)}
  .col-shop .cat-icon{left:10px;top:10px}
  .col-market .cat-icon{left:106px;top:47px}
  .banner-title{position:absolute;left:103px;top:100px;font-family:"Open Sans",sans-serif;color:var(--white);font-size:19px;line-height:26px;letter-spacing:.5px}
  .banner-faint{position:absolute;font-family:"Open Sans",sans-serif;color:rgba(255,255,255,.28);font-size:15px;line-height:18px;letter-spacing:.6px;white-space:nowrap}
  .section-bar{height:24px;background:linear-gradient(var(--green),var(--green-dark));color:var(--white);font-weight:700;font-size:14px;line-height:24px;padding-left:10px}
  .nav-item{height:72px;border-bottom:1px solid var(--line);font-size:13px;line-height:72px;padding-left:10px}
  .nav-item.active{background:var(--green-pale);border:0;position:relative}
  .nav-item.active svg{position:absolute;right:12px;top:29px}
  .pale-fill{background:var(--green-pale);height:40px}
  .world-title{position:absolute;left:20px;top:90px;color:var(--white);font-family:"Open Sans",sans-serif;font-size:28px;line-height:34px;letter-spacing:1px}
  .world-map{position:absolute;left:246px;top:8px;width:306px;height:156px;border-radius:28% 22% 30% 26%;
    background:linear-gradient(160deg,var(--map-light),var(--map-orange) 50%,var(--map-deep))}
  .tab-bar{height:24px;background:linear-gradient(var(--green),var(--green-dark));position:relative}
  .tab{position:absolute;left:0;top:0;height:24px;background:var(--white);padding:0 6px;font-size:14px;line-height:24px;color:#111}
  .tab-arrow{position:absolute;left:35px;top:27px}
  .listing{padding:0 12px}
  .dotted{border-top:1px dotted #999;margin-top:42px}
  .product-name{margin:20px 0 0 167px;color:var(--green-dark);font-weight:700;font-size:17px}
  .product-meta{margin:6px 0 0 167px;font-weight:700;font-size:13px}
  .more{margin:35px 0 0 14px;font-weight:700;font-size:14px}
  .pager{display:flex;justify-content:space-between;font-size:14px;margin-top:16px;padding-right:8px}
</style>
</head>
<body>
  <section class="column col-shop">
    <div class="banner">
      <div class="cat-icon" role="img" aria-label="Kategorie-Symbol Weltkarte"></div>
      <div class="banner-title">Landkarten und<br>Zubehör</div>
    </div>
    <div class="section-bar">Software</div>
    <div class="nav-item">GeoPlaner</div>
    <div class="nav-item">LIVE-DEMO</div>
    <div class="nav-item">SpotFinder (Standortsuche)</div>
    <div class="section-bar">Daten</div>
    <div class="pale-fill"></div>
  </section>

  <section class="column col-market">
    <div class="banner">
      <div class="cat-icon" role="img" aria-label="Kategorie-Symbol Weltkarte"></div>
      <div class="banner-faint" style="left:10px;top:136px">Topografische Karten</div>
      <div class="banner-faint" style="left:96px;top:154px">Administrative Karten</div>
    </div>
    <div class="section-bar">Marktdaten und Geodaten (GIS)</div>
    <div class="nav-item active">Marktdaten + Geodaten (GIS)
      <svg width="11" height="16" viewBox="0 0 11 16"><path d="M0 0L11 8L0 16Z" fill="#8cc34a"/></svg>
    </div>
  </section>

  <section class="column col-world">
    <div class="banner">
      <div class="banner-faint" style="left:48px;top:4px">Asien</div>
      <div class="banner-faint" style="left:18px;top:26px;font-size:20px;line-height:24px">Europa</div>
      <div class="banner-faint" style="left:136px;top:18px;font-size:14px">Afrika</div>
      <div class="banner-faint" style="left:66px;top:128px;font-size:13px">Australien</div>
      <div class="world-map" role="img" aria-label="Weltkarte mit orange eingefärbten Ländern"></div>
      <div class="banner-faint" style="left:212px;top:118px;font-size:20px;line-height:24px">Amerika</div>
      <div class="world-title">Welt-Edition</div>
    </div>
    <div class="tab-bar">
      <div class="tab">Kategorie 1</div>
      <svg class="tab-arrow" width="18" height="10" viewBox="0 0 18 10"><path d="M0 0H18L9 10Z" fill="#8cc34a"/></svg>
    </div>
    <div class="listing">
      <div class="dotted"></div>
      <div class="product-name">Marktdaten</div>
      <div class="product-meta">Nr.: &nbsp;· &nbsp;Größe:</div>
      <div class="more">mehr...</div>
      <div class="dotted" style="margin-top:30px"></div>
      <div class="pager"><span>Zeige <b>1</b> bis <b>1</b> (von insgesamt <b>1</b> Artikeln)</span><span>Seiten: &nbsp;<b>1</b></span></div>
    </div>
  </section>
</body>
</html>
```